Energy trading company (Voltrisa) needs a business card

We need a business card for a company based in Central America. Our main purpose is trading energy . We already have the logo but we need some good creativity to design a high impact business card. Colors blue, orange, green can be used or we would like to see good combinatios with our logo

Target Market(s)

Energy

Industry/Entity Type

Power Generation

Contact Information for Business Card

Logo , headquarters , name, background

Font styles to use
Serif
Sans Serif

Colors

Designer to choose colors to be used in the design.

Requirements
Must have
• it must have a fresh and clean view
Nice to have
• good backgrounds that combine with the logo
Should not have
• too much words

```html
<!DOCTYPE html>
<html lang="en">
<head>
<meta charset="utf-8">
<title>Voltrisa Business Card</title>
<link rel="stylesheet" href="https://fonts.googleapis.com/css2?family=Quicksand:wght@300;500;700&family=Lato:wght@400&display=swap">
<style>
  :root {
    --canvas-bg: #363636;
    --card-bg: #2f2f2f;
    --orange: #ee8e22;
    --orange-deep: #d97a18;
    --white: #f4f4f4;
    --soft-white: #e2e2e2;
  }
  html, body {
    margin: 0;
    padding: 0;
    width: 1200px;
    height: 1176px;
    overflow: hidden;
    background: var(--canvas-bg);
  }
  .canvas {
    position: relative;
    width: 1200px;
    height: 1176px;
  }
  .card {
    position: absolute;
    left: 290px;
    width: 620px;
    height: 352px;
    background: var(--card-bg);
    border-radius: 18px;
    overflow: hidden;
    box-shadow: 0 10px 24px rgba(0,0,0,0.35);
  }
  .card-back { top: 190px; }
  .card-front { top: 634px; }

  .brand {
    position: absolute;
    display: flex;
    align-items: center;
    gap: 14px;
    font-family: "Quicksand", sans-serif;
    font-weight: 500;
    color: var(--orange);
    letter-spacing: 1px;
  }
  .brand-mark {
    background: var(--orange);
    border-radius: 6px;
  }
  .card-back .brand { top: 52px; right: 40px; font-size: 40px; }
  .card-back .brand-mark { width: 30px; height: 30px; }

  .holder {
    position: absolute;
    left: 40px;
    top: 110px;
    font-family: "Quicksand", sans-serif;
  }
  .holder-name {
    margin: 0;
    font-weight: 700;
    font-size: 28px;
    color: var(--white);
  }
  .holder-title {
    margin: 4px 0 0;
    font-weight: 300;
    font-size: 19px;
    color: var(--orange);
    letter-spacing: 0.5px;
  }
  .divider {
    position: absolute;
    left: 150px;
    right: 26px;
    top: 166px;
    height: 2px;
    background: var(--orange);
  }
  .contacts {
    position: absolute;
    left: 40px;
    top: 196px;
    margin: 0;
    padding: 0;
    list-style: none;
    font-family: "Lato", sans-serif;
    font-size: 17px;
    color: var(--soft-white);
  }
  .contacts li {
    display: flex;
    align-items: center;
    gap: 12px;
    height: 27px;
  }
  .contacts svg { width: 14px; height: 14px; }
  .address {
    position: absolute;
    right: 30px;
    bottom: 40px;
    font-family: "Lato", sans-serif;
    font-size: 16px;
    color: var(--soft-white);
  }
  .band {
    position: absolute;
    left: 0;
    right: 0;
    bottom: 0;
    height: 22px;
    background: linear-gradient(90deg, var(--orange-deep), var(--orange));
  }

  .brand-panel {
    position: absolute;
    left: 0;
    top: 0;
    width: 352px;
    height: 352px;
    background: linear-gradient(200deg, var(--orange) 0%, var(--orange-deep) 100%);
  }
  .card-front .brand {
    left: 356px;
    bottom: 24px;
    font-size: 46px;
    letter-spacing: 0.5px;
  }
</style>
</head>
<body>
<main class="canvas">
  <section class="card card-back" aria-label="Card back with contact details">
    <div class="brand"><span class="brand-mark"></span>VOLTRISA</div>
    <div class="holder">
      <p class="holder-name">Your Name</p>
      <p class="holder-title">JOB TITLE</p>
    </div>
    <div class="divider"></div>
    <ul class="contacts">
      <li>
        <svg viewBox="0 0 14 14"><path d="M3 1 L5.5 1 L6 4 L4.5 5 Q5.5 8 9 9.5 L10 8 L13 8.5 L13 11 Q12 13 9.5 12.5 Q3 10.5 1.5 4 Q1.5 1.5 3 1 Z" fill="#ee8e22"/></svg>
        000 000 0000
      </li>
      <li>
        <svg viewBox="0 0 14 14"><rect x="1" y="3" width="12" height="8" fill="#ee8e22"/><path d="M1 3 L7 8 L13 3" stroke="#2f2f2f" stroke-width="1.2" fill="none"/></svg>
        youremai@xyz.com
      </li>
      <li>
        <svg viewBox="0 0 14 14" fill="none" stroke="#ee8e22" stroke-width="1.2"><circle cx="7" cy="7" r="5.5"/><ellipse cx="7" cy="7" rx="2.4" ry="5.5"/><path d="M1.5 7 H12.5 M2.5 4 H11.5 M2.5 10 H11.5"/></svg>
        www.yourwebsite.com
      </li>
    </ul>
    <div class="address">000, Street Name, City, ST 0000</div>
    <div class="band"></div>
  </section>

  <section class="card card-front" aria-label="Card front">
    <div class="brand-panel" role="img" aria-label="Large brand symbol area"></div>
    <div class="brand">VOLTRISA</div>
  </section>
</main>
</body>
</html>
```